Drone company needs a brochure design

We would like a brochure design which compliments our existing logo, website and business card designs.

www.tallowmerrin.com.au

Business

```html
<!DOCTYPE html>
<html lang="en">
<head>
<meta charset="utf-8">
<title>Tallow Merrin – UAV Services Brochure</title>
<link rel="stylesheet" href="https://fonts.googleapis.com/css2?family=Orbitron:wght@700;800&family=Exo+2:wght@600&family=Roboto+Condensed:wght@400&family=Roboto:wght@400&display=swap">
<style>
  :root{
    --blue:#29a8e0;
    --blue-dark:#1b7fb0;
    --black:#151515;
    --ink:#222222;
    --white:#ffffff;
    --paper:#fafafa;
    --stage:#e9e9e9;
    --photo-grey-1:#d8d8d8;
    --photo-grey-2:#8e8e8e;
    --photo-green-1:#6f9b4a;
    --photo-green-2:#2f5a2a;
  }
  html,body{margin:0;padding:0;width:907px;height:1200px;overflow:hidden;background:var(--stage);}
  .brochure{
    position:absolute;left:128px;top:24px;
    width:591px;height:1047px;
    transform:scale(1.1);transform-origin:0 0;
    background:var(--paper);overflow:hidden;
    font-family:"Roboto Condensed",sans-serif;
  }
  .artwork{position:absolute;left:0;top:0;width:591px;height:1047px;}
  .brand{
    position:absolute;left:14px;top:70px;
    display:flex;align-items:center;gap:7px;
    font-family:"Roboto",sans-serif;font-size:20px;color:var(--ink);
  }
  .brand-dot{width:10px;height:10px;border-radius:50%;background:var(--blue);}
  .drone-photo{
    position:absolute;left:388px;top:27px;width:180px;height:125px;
    background:radial-gradient(ellipse at 50% 50%,#d9d2c4 0%,#9a9590 45%,#f4f4f4 80%);
  }
  .headline{position:absolute;left:0;width:591px;text-align:center;margin:0;}
  .headline-lead{
    top:647px;font-family:"Orbitron",sans-serif;font-weight:800;
    font-size:24px;letter-spacing:1px;color:var(--blue);padding-left:10px;box-sizing:border-box;
  }
  .headline-sub{
    top:677px;font-family:"Exo 2",sans-serif;font-weight:600;
    font-size:27px;letter-spacing:.5px;color:var(--white);
  }
  .services-title{
    position:absolute;left:133px;top:741px;width:330px;text-align:center;margin:0;
    font-family:"Orbitron",sans-serif;font-weight:800;font-size:29px;letter-spacing:1px;color:var(--white);
  }
  .service-list{
    position:absolute;list-style:none;margin:0;padding:0;
    font-size:25px;line-height:30px;color:var(--ink);
  }
  .service-list.left{left:48px;top:811px;}
  .service-list.right{left:333px;top:805px;}
  .service-list li{position:relative;padding-left:18px;margin-bottom:3px;}
  .service-list li::before{
    content:"";position:absolute;left:0;top:11px;width:9px;height:7px;
    background:var(--blue);transform:skewY(-25deg);
  }
  .contact{
    position:absolute;display:flex;align-items:center;gap:6px;
    font-family:"Roboto",sans-serif;font-size:15px;color:var(--white);
  }
  .contact svg{width:15px;height:15px;flex:none;}
  .contact.phone{left:30px;top:989px;}
  .contact.email{left:30px;top:1009px;}
  .contact.web{left:326px;top:1009px;}
</style>
</head>
<body>
<main class="brochure">
  <svg class="artwork" viewBox="0 0 591 1047" xmlns="http://www.w3.org/2000/svg">
    <defs>
      <linearGradient id="cityTone" x1="0" y1="0" x2="0" y2="1">
        <stop offset="0" stop-color="var(--photo-grey-1)"/>
        <stop offset="1" stop-color="var(--photo-grey-2)"/>
      </linearGradient>
      <linearGradient id="parkTone" x1="0" y1="0" x2="1" y2="1">
        <stop offset="0" stop-color="var(--photo-green-1)"/>
        <stop offset="1" stop-color="var(--photo-green-2)"/>
      </linearGradient>
    </defs>
    <g role="img" aria-label="Grey-toned aerial photograph of a suburban town">
      <rect x="0" y="362" width="591" height="265" fill="url(#cityTone)"/>
    </g>
    <polygon class="band-black" points="0,352 283,572 591,350 591,375 283,602 0,378" fill="var(--black)"/>
    <polygon class="band-blue" points="0,277 283,500 591,277 591,350 283,580 0,352" fill="var(--blue)"/>
    <polygon class="frame-outer" points="305,10 541,270 283,507 43,250" fill="var(--black)"/>
    <polygon class="frame-gap" points="305,18 532,270 283,498 52,250" fill="var(--white)"/>
    <g role="img" aria-label="Aerial photograph of a park with lawns, trees and buildings">
      <polygon points="252,80 358,80 524,270 283,490 60,250" fill="url(#parkTone)"/>
    </g>
    <polygon class="frame-accent" points="305,24 254,80 356,80" fill="var(--blue)"/>
    <rect class="title-bar" x="0" y="627" width="591" height="110" fill="var(--black)"/>
    <polygon class="services-tab-edge" points="128,732 468,732 448,786 148,786" fill="var(--blue-dark)"/>
    <polygon class="services-tab" points="160,732 436,732 436,786 160,786" fill="var(--blue)"/>
    <rect class="footer-rule" x="0" y="957" width="591" height="6" fill="var(--blue)"/>
    <rect class="footer" x="0" y="966" width="591" height="81" fill="var(--black)"/>
  </svg>

  <div class="brand"><span class="brand-dot"></span>Tallow Merrin</div>
  <div class="drone-photo" role="img" aria-label="Photograph of a camera drone in flight"></div>

  <h1 class="headline headline-lead">LATEST UNMANNED AERIAL</h1>
  <h2 class="headline headline-sub">VEHICLES (UAV)&nbsp; TECHNOLOGY</h2>

  <h3 class="services-title">SERVICES</h3>
  <ul class="service-list left">
    <li>Real Estate</li>
    <li>Construction<br>&amp; Property</li>
    <li>Media &amp; Advertising</li>
  </ul>
  <ul class="service-list right">
    <li>Inspection &amp;<br>Environment</li>
    <li>Survey &amp; Mapping</li>
    <li>Insurance &amp; Risk</li>
  </ul>

  <div class="contact phone">
    <svg viewBox="0 0 16 16"><rect width="16" height="16" rx="3" fill="var(--blue)"/><path d="M5 3.5l2 2-1 1.2c.6 1.3 1.6 2.3 2.9 2.9l1.2-1 2 2-1.3 1.6C7.4 12 4 8.6 3.4 5z" fill="var(--white)"/></svg>
    040 555 0187
  </div>
  <div class="contact email">
    <svg viewBox="0 0 16 16"><rect y="3" width="16" height="11" rx="1.5" fill="var(--blue)"/><path d="M1 4.5l7 5 7-5" stroke="var(--white)" stroke-width="1.4" fill="none"/></svg>
    contact@tallowmerrin.com.au
  </div>
  <div class="contact web">
    <svg viewBox="0 0 16 16"><circle cx="8" cy="8" r="6.5" fill="var(--blue)"/><path d="M1.5 8h13M8 1.5c2.5 2.5 2.5 10.5 0 13M8 1.5c-2.5 2.5-2.5 10.5 0 13" stroke="var(--black)" stroke-width="1" fill="none"/></svg>
    www.tallowmerrin.com.au
  </div>
</main>
</body>
</html>
```